Mesa Lumbre, Mexican Restaurant Menu

We need a menu design for a Mexican Restaurant in Dubai UAE

The concept of the Restaurant is as a Mexican Taqueria, That is simple street food like tacos, burritos, quesadillas, etc

We want a menu that is fun to read and that keeps a casual / street / urban feeling.If possible on a single page or 2 maximum so we can print on both sides and have it laminated

We are attaching photos of our logo and of the food that we will be serving, we are open to ideas and suggestions to try to make this as fun/casual as possible.

Also attaching photos of the style of tables we will use at the restaurant

Please avoid using tex mex items, like Crispy Taco Shells, Chiili, Cheddar Cheese , Fajitas, etc

Prices are not yet decided in the meantime you can use any price for the menu items.

If you can not include a photo for any single item on the menu, or you think it wouldn't look good, the ones that must be are.

1.-Tacos Al Pastor (this is the star of the show)
2-Guacamole
3-Burritos
4- Some Specials and alambres (photos attached)

Menu Items should have the description of ingredients on english and spanish (attached in menu file)

Any other idea or phrase trying to keep it fun and to show people that this is authentic mexican food and not tex mex would be nice to have.

If you have any doubts please contact us! Thanks for your help!

Target Market(s)

Expats living in Dubai + Latin Community,

Industry/Entity Type

Mexican Restaurant

Font styles to use
Other font styles liked:
• Helsinki, Helvetica , Klinic Slab

Colors
33a6d7
ec1f27
0455a3
fbee3d
9bcb3b
cadf82
f59195
85cae6
e34297

Requirements
Must have
• Fun to read, Preference on a Single page or 2 so we can print on both sides Or a Tri Fold so we can also use it for our Home Delivery Take away menu. Photos , Item ingredients in Spanish/English (attached on the menu file)
Nice to have
• Fun phrases, Reference to mexican food or characters
Should not have
• Tex Mex Items like Taco Shells , Chiili con Carne, Cheddar cheese

```html
<!DOCTYPE html>
<html lang="en">
<head>
<meta charset="utf-8">
<title>Mesa Lumbre — Menu</title>
<link href="https://fonts.googleapis.com/css2?family=Rye&family=Kaushan+Script&family=Baloo+2:wght@800&display=swap" rel="stylesheet">
<style>
  :root {
    --red: #ec1f27;
    --aqua: #62e9f0;
    --wood-light: #e9b6a4;
    --wood-dark: #b98272;
    --paper-center: #f1e6dc;
    --paper-mid: #e6d3b8;
    --paper-edge: #c49b45;
    --frame: #f6e2d8;
    --photo-warm: #8a5a2b;
    --photo-green: #7bb33a;
  }
  * { margin: 0; padding: 0; box-sizing: border-box; }
  html, body { width: 1200px; height: 1000px; overflow: hidden; background: #ffffff; }
  .menu { position: relative; width: 1200px; height: 1000px; overflow: hidden; }
  .wood-backdrop {
    position: absolute; left: 25px; top: 25px; width: 1150px; height: 975px;
    background:
      repeating-linear-gradient(90deg, rgba(120,60,50,.18) 0 2px, transparent 2px 165px),
      linear-gradient(90deg, var(--wood-dark), var(--wood-light) 8%, var(--wood-light) 92%, var(--wood-dark));
  }
  .paper {
    position: absolute; left: 85px; top: 73px; width: 1030px; height: 927px;
    background: radial-gradient(ellipse 60% 70% at 50% 55%, var(--paper-center) 0%, var(--paper-mid) 60%, var(--paper-edge) 100%);
    text-align: center;
    color: var(--red);
  }
  .brand-mark {
    position: absolute; left: 50%; top: 52px; width: 26px; height: 26px;
    margin-left: -13px; border: 3px solid var(--red);
  }
  .brand-name {
    position: absolute; left: 0; right: 0; top: 150px;
    font-family: "Rye", serif; font-size: 76px; line-height: 1; color: var(--red);
    letter-spacing: 1px;
  }
  .tagline {
    position: absolute; left: 0; right: 0; top: 275px;
    font-family: "Baloo 2", sans-serif; font-weight: 800; font-size: 20px;
    letter-spacing: 4px; color: var(--red);
  }
  .section-title {
    position: absolute; left: 0; right: 0; top: 398px;
    font-family: "Kaushan Script", cursive; font-size: 46px; color: var(--aqua);
  }
  .items { position: absolute; left: 0; right: 0; top: 512px; font-family: "Kaushan Script", cursive; }
  .item { margin-bottom: 22px; }
  .item-name { font-size: 21px; line-height: 1.25; }
  .item-desc { font-size: 15px; line-height: 1.3; }
  .photo {
    position: absolute; padding: 14px; background: var(--frame);
    box-shadow: 0 2px 6px rgba(0,0,0,.25);
  }
  .photo-fill { width: 100%; height: 100%; }
  .photo-queso { left: 92px; top: 500px; width: 200px; height: 150px; transform: rotate(-8deg); }
  .photo-queso .photo-fill { background: radial-gradient(circle at 50% 50%, #e8b04a, var(--photo-warm) 55%, #2a1a14); }
  .photo-guac { left: 762px; top: 472px; width: 205px; height: 145px; transform: rotate(9deg); }
  .photo-guac .photo-fill { background: radial-gradient(circle at 50% 45%, var(--photo-green), #a5672e 65%, #c23a2a); }
</style>
</head>
<body>
<main class="menu">
  <div class="wood-backdrop" role="img" aria-label="Pink-toned wooden plank backdrop"></div>
  <section class="paper">
    <div class="brand-mark"></div>
    <h1 class="brand-name">MESA LUMBRE</h1>
    <p class="tagline">URBAN MEXICAN FOOD</p>
    <h2 class="section-title">La Botana / Appetizers</h2>

    <figure class="photo photo-queso"><div class="photo-fill" role="img" aria-label="Photo of melted queso fundido in a skillet"></div></figure>
    <figure class="photo photo-guac"><div class="photo-fill" role="img" aria-label="Photo of guacamole bowl with tortilla chips"></div></figure>

    <div class="items">
      <div class="item"><p class="item-name">Rafa’s Famous Guacamole with Chips</p></div>
      <div class="item">
        <p class="item-name">Queso Fundido/Melted Cheese</p>
        <p class="item-desc">Plain or with Champinones/Mushrooms</p>
      </div>
      <div class="item">
        <p class="item-name">Nachos</p>
        <p class="item-desc">De Pastor – Tower of chips covered with cheese , beans, jalapenos and our Famous Pastor</p>
        <p class="item-desc">De Bistek – Tower of chips covered with cheese , beans, jalapenos and Delicious Steak</p>
        <p class="item-desc">Tradicional– Tower of chips covered with cheese, beans, and jalapenos</p>
      </div>
      <div class="item">
        <p class="item-name">Sopes</p>
        <p class="item-desc">Frijol/Refried Beans, bistek/steak o pollo/chicken</p>
      </div>
      <div class="item">
        <p class="item-name">Quesadillas</p>
        <p class="item-desc">Tradicional/Plain, Con Pollo/Chicken o Veggie</p>
      </div>
    </div>
  </section>
</main>
</body>
</html>
```